A letter fromthe tooth fairy

We our looking for a design of a fairy (tooth fairy) its for a letter we our doing. The letter is a note from the tooth fairy. We already have the wording done we just need the fairy and the board of the letter done! We want the fairy to be a woman with some age to her and we want her to look magical but not futuristic , also we want her charming but not sexy this is for small children. We also would like the boarder of the letter to look magical. Last the fairy needs to be at angle like flying. The angle needs to be a little to the right (I guess what I mean is if you were looking at a clock her head would be at 1or 2 on a clock and her feet at 7or 8 on a clock.
Reason: To allow the adjustments to designs summited .

```html
<!DOCTYPE html>
<html lang="en">
<head>
<meta charset="utf-8">
<title>A Letter from the Tooth Fairy</title>
<link rel="stylesheet" href="https://fonts.googleapis.com/css2?family=Handlee&display=swap">
<style>
  :root {
    --paper: #ffffff;
    --ink: #000000;
    --swirl-blue: #9ec6ee;
    --swirl-pink: #f2b8ea;
    --fairy-yellow: #f3f0a0;
    --fairy-blue: #3b63d6;
    --fairy-pink: #f7cfe6;
  }
  html, body {
    margin: 0;
    padding: 0;
    width: 848px;
    height: 1200px;
    overflow: hidden;
    background: var(--paper);
  }
  .letter {
    position: relative;
    width: 848px;
    height: 1200px;
    background: var(--paper);
    overflow: hidden;
  }
  .fairy-illustration {
    position: absolute;
    left: 25px;
    top: 14px;
    width: 240px;
    height: 320px;
  }
  .corner-ornament {
    position: absolute;
  }
  .corner-ornament--top-right {
    right: 10px;
    top: 0;
    width: 300px;
    height: 276px;
  }
  .corner-ornament--bottom-left {
    left: 0;
    bottom: 0;
    width: 304px;
    height: 316px;
  }
  .corner-ornament--bottom-right {
    right: 6px;
    bottom: 0;
    width: 264px;
    height: 316px;
  }
  .letter-body {
    position: absolute;
    left: 102px;
    top: 446px;
    width: 500px;
    margin: 0;
    font-family: "Handlee", cursive;
    font-size: 31px;
    line-height: 42.5px;
    color: var(--ink);
  }
  .letter-body p {
    margin: 0;
  }
  .signature {
    margin-top: 42px !important;
  }
</style>
</head>
<body>
  <main class="letter">
    <svg class="fairy-illustration" viewBox="0 0 240 320" role="img" aria-label="Illustration of a flying tooth fairy with blonde hair, translucent wings and a blue polka-dot dress, holding a large white tooth">
      <defs>
        <linearGradient id="fairyTones" x1="0" y1="0" x2="0.6" y2="1">
          <stop offset="0" stop-color="var(--fairy-yellow)"/>
          <stop offset="0.5" stop-color="var(--fairy-pink)"/>
          <stop offset="1" stop-color="var(--fairy-blue)" stop-opacity="0.55"/>
        </linearGradient>
      </defs>
      <rect x="0" y="0" width="240" height="320" rx="40" fill="url(#fairyTones)"/>
    </svg>

    <svg class="corner-ornament corner-ornament--top-right" viewBox="0 0 300 276" role="img" aria-label="Magical corner ornament of blue swirls with colourful stars and confetti">
      <defs>
        <radialGradient id="swirlTopRight" cx="0.8" cy="0.2" r="0.9">
          <stop offset="0" stop-color="var(--swirl-blue)"/>
          <stop offset="0.6" stop-color="var(--swirl-pink)" stop-opacity="0.5"/>
          <stop offset="1" stop-color="var(--paper)" stop-opacity="0"/>
        </radialGradient>
      </defs>
      <rect width="300" height="276" fill="url(#swirlTopRight)"/>
    </svg>

    <svg class="corner-ornament corner-ornament--bottom-left" viewBox="0 0 304 316" role="img" aria-label="Magical corner ornament of blue swirls with colourful stars and confetti">
      <defs>
        <radialGradient id="swirlBottomLeft" cx="0.2" cy="0.8" r="0.9">
          <stop offset="0" stop-color="var(--swirl-blue)"/>
          <stop offset="0.6" stop-color="var(--swirl-pink)" stop-opacity="0.5"/>
          <stop offset="1" stop-color="var(--paper)" stop-opacity="0"/>
        </radialGradient>
      </defs>
      <rect width="304" height="316" fill="url(#swirlBottomLeft)"/>
    </svg>

    <svg class="corner-ornament corner-ornament--bottom-right" viewBox="0 0 264 316" role="img" aria-label="Magical corner ornament of blue swirls with colourful stars and confetti">
      <defs>
        <radialGradient id="swirlBottomRight" cx="0.8" cy="0.8" r="0.9">
          <stop offset="0" stop-color="var(--swirl-blue)"/>
          <stop offset="0.6" stop-color="var(--swirl-pink)" stop-opacity="0.5"/>
          <stop offset="1" stop-color="var(--paper)" stop-opacity="0"/>
        </radialGradient>
      </defs>
      <rect width="264" height="316" fill="url(#swirlBottomRight)"/>
    </svg>

    <article class="letter-body">
      <p>Congratulations! I heard you lost your<br>first tooth. So I had to come check for<br>myself. Looks great, so I left you a<br>surprise under your pillow. Keep up the<br>good work on brushing your teeth at<br>least twice a day! I will be visiting you<br>again on another day!</p>
      <p class="signature">The Tooth Fairy</p>
    </article>
  </main>
</body>
</html>
```